Quiz Company needs two PDF sheets designing

We need two different A4 sheets to be designed - similar to those attached - they need to be at least two-coloured - A4 horizontal layout

The Bingo sheet is as per the attached Word mock up and is similar to the Bingo PDF attached

The Cellraiders sheet should feature 24 hexagons in 6 vertical rows of 4 hexagons

Font styles to use
Serif

Requirements
Must have
• PDF file at least two colours
• www.pubpuzzlers.co.uk - 01632 960481 and our logo somewhere on the sheet
Nice to have
• Right Hand Side - Bingo - A Six x Six Grid of round squares with space to write numbers and answers in
• Left Hand side - Space for instructions Numbers 1 to 36 with space for answers - then a mini grid with just circles and space to write numbers in see attached mock up.
• Cellraiders - Right hand side will be 6 lines of 4 hexagons all connecting as per the example - top left numbers 1 to 24 and a small grid for just numbers
• Both sheets also have instructions

```html
<!DOCTYPE html>
<html lang="en">
<head>
<meta charset="utf-8">
<title>Cellraiders Quiz Sheet</title>
<link rel="stylesheet" href="https://fonts.googleapis.com/css2?family=Arimo:wght@400;700&family=Cabin:wght@400&family=Alfa+Slab+One&family=Roboto+Slab:wght@700&display=swap">
<style>
  :root {
    --ink: #5f63ad;
    --ink-soft: #6b6fb5;
    --number: #5a5e8c;
    --frame: #9a9a9a;
    --paper: #ffffff;
  }
  * { box-sizing: border-box; margin: 0; padding: 0; }
  html, body { width: 1200px; height: 848px; overflow: hidden; background: var(--paper); }
  .sheet {
    position: relative; width: 1200px; height: 848px;
    border: 1px solid var(--frame); background: var(--paper);
    font-family: "Arimo", Arial, sans-serif; color: var(--ink);
  }
  .answer-panel {
    position: absolute; left: 21px; top: 27px; width: 361px; height: 794px;
    border: 1px solid var(--ink-soft);
  }
  .answer-list { list-style: none; position: absolute; left: 35px; top: 12px; width: 290px; }
  .answer-row {
    height: 20px; margin-bottom: 4.55px; border: 1px solid var(--ink-soft);
    font-size: 10.5px; line-height: 18px; padding-left: 13px; color: var(--number);
  }
  .panel-divider { position: absolute; left: 0; right: 0; top: 607px; border-top: 1px solid var(--ink-soft); }
  .mini-team {
    position: absolute; left: 37px; top: 771px;
    font-family: "Roboto Slab", Georgia, serif; font-size: 6.5px; font-weight: 700; line-height: 8px; color: var(--ink);
  }
  .play-panel {
    position: absolute; left: 422px; top: 27px; width: 757px; height: 794px;
    border: 1px solid var(--ink-soft);
  }
  .brand { position: absolute; left: 26px; top: 56px; display: flex; align-items: center; gap: 8px; }
  .brand-dot { width: 26px; height: 26px; border-radius: 50%; background: var(--ink); }
  .brand-name { font-family: "Roboto Slab", Georgia, serif; font-weight: 700; font-size: 24px; color: var(--ink); }
  .title {
    position: absolute; right: 23px; top: 52px;
    font-family: "Alfa Slab One", Georgia, serif; font-weight: 400; font-size: 36px; color: var(--ink); letter-spacing: 0.5px;
  }
  .instructions {
    position: absolute; left: 22px; top: 159px; width: 711px;
    font-family: "Cabin", sans-serif; font-size: 9.4px; line-height: 14px; text-align: justify; color: var(--ink);
  }
  .team-name {
    position: absolute; left: 24px; top: 680px;
    font-family: "Roboto Slab", Georgia, serif; font-size: 15.5px; font-weight: 700; line-height: 18px; color: var(--ink);
  }
  .contact {
    position: absolute; right: 24px; top: 740px; text-align: right;
    font-family: "Roboto Slab", Georgia, serif; font-size: 13px; font-weight: 700; line-height: 18px; color: var(--ink);
  }
  .hex-grid { position: absolute; left: 0; top: 0; width: 1200px; height: 848px; pointer-events: none; }
  .hex-big { fill: none; stroke: var(--ink); stroke-width: 3; }
  .hex-mini { fill: none; stroke: var(--ink); stroke-width: 1.3; }
  .no-big { font-family: "Arimo", Arial, sans-serif; font-size: 10px; font-weight: 700; fill: var(--ink); }
  .no-mini { font-family: "Arimo", Arial, sans-serif; font-size: 5px; fill: var(--ink); }
</style>
</head>
<body>
<div class="sheet">
  <section class="answer-panel">
    <ol class="answer-list">
      <li class="answer-row">1</li><li class="answer-row">2</li><li class="answer-row">3</li><li class="answer-row">4</li>
      <li class="answer-row">5</li><li class="answer-row">6</li><li class="answer-row">7</li><li class="answer-row">8</li>
      <li class="answer-row">9</li><li class="answer-row">10</li><li class="answer-row">11</li><li class="answer-row">12</li>
      <li class="answer-row">13</li><li class="answer-row">14</li><li class="answer-row">15</li><li class="answer-row">16</li>
      <li class="answer-row">17</li><li class="answer-row">18</li><li class="answer-row">19</li><li class="answer-row">20</li>
      <li class="answer-row">21</li><li class="answer-row">22</li><li class="answer-row">23</li><li class="answer-row">24</li>
    </ol>
    <div class="panel-divider"></div>
    <p class="mini-team">TEAM<br>NAME</p>
  </section>

  <section class="play-panel">
    <div class="brand"><span class="brand-dot"></span><span class="brand-name">Pub Puzzlers</span></div>
    <h1 class="title">Cellraiders Quiz</h1>
    <p class="instructions">The quiz master will call out questions from 1 to 24 – write the number of the question and the answer to it in ANY hexagon below and copy the answer against the correct number on the left. Also write the numbers you use in the corresponding hexagons bottom left. Once all questions have been read out, tear off the left hand side and hand to the quizmaster. They will now read out the answers in a random order – you need to get a straight line of six answers from any of the four cells on the left to any of the four cells on the right – once you have them shout “CELLRAIDER” and the quizmaster will check your sheet – Good Luck – anyone seen with a mobile phone will have it smashed to pieces with a hammer and will be disqualified!</p>
    <p class="team-name">TEAM<br>NAME</p>
    <p class="contact">www.pubpuzzlers.co.uk<br>01632 960481</p>
  </section>

  <svg class="hex-grid" viewBox="0 0 1200 848" aria-hidden="true">
    <defs>
      <g id="cell-big">
        <polygon class="hex-big" points="-48,0 -24,-41.6 24,-41.6 48,0 24,41.6 -24,41.6"/>
        <text class="no-big" x="-26" y="-26">No.</text>
      </g>
      <g id="cell-mini">
        <polygon class="hex-mini" points="-20,0 -10,-17.3 10,-17.3 20,0 10,17.3 -10,17.3"/>
        <text class="no-mini" x="-11" y="-10">No.</text>
      </g>
    </defs>
    <g class="board">
      <use href="#cell-big" x="600" y="332"/><use href="#cell-big" x="600" y="423"/><use href="#cell-big" x="600" y="514"/><use href="#cell-big" x="600" y="605"/>
      <use href="#cell-big" x="680" y="377"/><use href="#cell-big" x="680" y="468"/><use href="#cell-big" x="680" y="559"/><use href="#cell-big" x="680" y="650"/>
      <use href="#cell-big" x="760" y="332"/><use href="#cell-big" x="760" y="423"/><use href="#cell-big" x="760" y="514"/><use href="#cell-big" x="760" y="605"/>
      <use href="#cell-big" x="840" y="377"/><use href="#cell-big" x="840" y="468"/><use href="#cell-big" x="840" y="559"/><use href="#cell-big" x="840" y="650"/>
      <use href="#cell-big" x="920" y="332"/><use href="#cell-big" x="920" y="423"/><use href="#cell-big" x="920" y="514"/><use href="#cell-big" x="920" y="605"/>
      <use href="#cell-big" x="1000" y="377"/><use href="#cell-big" x="1000" y="468"/><use href="#cell-big" x="1000" y="559"/><use href="#cell-big" x="1000" y="650"/>
    </g>
    <g class="mini-board">
      <use href="#cell-mini" x="130" y="658"/><use href="#cell-mini" x="130" y="696"/><use href="#cell-mini" x="130" y="734"/><use href="#cell-mini" x="130" y="772"/>
      <use href="#cell-mini" x="164" y="677"/><use href="#cell-mini" x="164" y="715"/><use href="#cell-mini" x="164" y="753"/><use href="#cell-mini" x="164" y="791"/>
      <use href="#cell-mini" x="198" y="658"/><use href="#cell-mini" x="198" y="696"/><use href="#cell-mini" x="198" y="734"/><use href="#cell-mini" x="198" y="772"/>
      <use href="#cell-mini" x="232" y="677"/><use href="#cell-mini" x="232" y="715"/><use href="#cell-mini" x="232" y="753"/><use href="#cell-mini" x="232" y="791"/>
      <use href="#cell-mini" x="266" y="658"/><use href="#cell-mini" x="266" y="696"/><use href="#cell-mini" x="266" y="734"/><use href="#cell-mini" x="266" y="772"/>
      <use href="#cell-mini" x="300" y="677"/><use href="#cell-mini" x="300" y="715"/><use href="#cell-mini" x="300" y="753"/><use href="#cell-mini" x="300" y="791"/>
    </g>
  </svg>
</div>
</body>
</html>
```